IT Company needs functional Word Press/Web Design

Our primary goal is to make an additional website to our existing website. This site will be used as a quotation database for our products. We require this site to be fully functional (design and coding).

It would be ideal if one designer is able to code and design a site, however If this needs to be completed as two seperate projects we are willing to take that path.

If this seems like something you would be interested in please click the link/file uploaded brief to see a more detailed brief of what are after.

**Please do not submit designs at this stage if you are not able to code a fully functional site.

We look forward to seeing what you can come up with.
Thank you .

Requirements
Must have
• *Must be fully functional and as per our brief

* Website must be uploaded and running (We will supply cpanel and hosting details)

*To create a current customer resource site for them to access custom designed quotes or browse existing quotes

*All source and graphics/files included

*To integrate with email marketing

*To integrate with social media

*To provide a high quality and 'simple' to use site

*To 'eventually' build a product database that may be marketed via Chirpnet, Friendloop or e-mail marketing campaigns

*To provide professional quotes to our existing clients with the future outlook to build our retail side of the business

*Individual URL's to products (quotes)

*Private and public quotes (private can simply be a URL that is not linked or displayed on the main site)

*Ability to (from product / quote page) 'Post to Friendloop', 'Chirp to Chirpnet', 'email myself or a friend', 'print' and 'download a PDF' - then if this could somehow be monitored or if we could somehow be notified when someone requests to have a quote emailed so that we are able to follow it up in the future?

*In all of the above options apart from the social media ones we require a High-Quality PDF to be generated with the product(s) that will look nice if printed

*Ability to cross-link products or have options for 'accessories' i.e. a Printer may have links to toner cartridges or an extended warranty item

*It will have to be accessible for cross devices for example on an ipad, and all movile devices (be able to load all of the logos etc).

*Sign up to mailing list option/ update on news/changes to this product – i.e. on every product page
Nice to have
• *Design of website

*Ability to actually purchase products via (Remitly Pay payment?) or simply 'place order' for existing customers (we would then send them an invoice as normal)

*We would like this page to provide our contact details

* A product search section/option

We like the look and social integration features of some of the templates on: http://www.cartobloom.com/examples

Having said that, it will need to meet the other requirements of our brief. But it might be a good platform to build from?

i.e. (Vendralo Templates)

http://shop.brightmeadowgoods.com/

http://www.pelltanner.com/#/collection/heritage

http://shop.thewanderingkeelguild.com// **Simple and neat

http://quietfernbrew.com/ **Like hover over info on products – not too busy.

Should not have
• Bad examples

http://www.voltabench.co.nz/

http://www.gadrimtek.com/

* Please note that we also want a customised design.

We don't want anything too complex or busy.

```html
<!DOCTYPE html>
<html lang="en">
<head>
<meta charset="utf-8">
<title>ByteGuard IT Consulting</title>
<link rel="stylesheet" href="https://fonts.googleapis.com/css2?family=Oswald:wght@400;500&family=Lato:wght@400;700&family=Open+Sans:wght@400;600&display=swap">
<style>
:root{
  --dark:#1c1d1f;
  --dark-2:#2a2c2f;
  --page:#e6e4e2;
  --blue:#1d4a8c;
  --blue-light:#2c63b0;
  --blue-deep:#173c75;
  --accent:#3d8fd6;
  --white:#ffffff;
  --text:#333333;
  --muted:#666666;
  --gold:#f2a623;
  --card:#ffffff;
  --line:#d6d6d6;
}
*{box-sizing:border-box;margin:0;padding:0}
html,body{width:1087px;height:1200px;overflow:hidden}
body{position:relative;background:var(--page);font-family:"Open Sans",Arial,sans-serif;color:var(--text)}
.top-band{position:absolute;left:0;top:0;width:1087px;height:450px;background:radial-gradient(ellipse at 30% 40%,#3a3c40 0%,var(--dark) 60%,#111 100%)}
.abs{position:absolute}
.logo{left:178px;top:58px;display:flex;align-items:center;gap:10px}
.logo-mark{width:30px;height:30px;background:var(--accent)}
.logo-name{font-family:"Lato",sans-serif;font-weight:700;font-size:27px;color:var(--accent);letter-spacing:1px}
.logo-tag{left:345px;top:87px;font-family:"Lato",sans-serif;font-size:8px;letter-spacing:3px;color:#9a9a9a}
.account{left:782px;top:79px;display:flex;gap:8px}
.account a{display:block;height:20px;line-height:20px;border-radius:10px;font-size:10px;color:var(--white);text-decoration:none;text-align:center}
.signin{width:63px;background:#2d2f33}
.register{width:63px;background:var(--blue-light)}
.nav{left:170px;top:115px;width:746px;height:58px;background:linear-gradient(#2d62ad,var(--blue));border-radius:6px 6px 0 0;display:flex;align-items:center}
.nav-home{width:50px;height:100%;display:flex;align-items:center;justify-content:center;border-right:1px solid #3a6fba}
.nav a.item{font-family:"Oswald",sans-serif;font-size:13px;color:var(--white);text-decoration:none;padding:0 12px;height:100%;line-height:58px;border-right:1px solid #3a6fba}
.nav a.item:last-of-type{border-right:none}
.nav-search{position:absolute;right:16px;top:20px;width:140px;height:18px;background:var(--white);border-radius:9px;font-size:9px;color:var(--accent);padding:3px 0 0 16px;letter-spacing:1px}
.nav-search svg{position:absolute;right:10px;top:3px}
.hero{left:170px;top:173px;width:746px;height:277px;background:linear-gradient(180deg,#6e9bd0 0%,#a9c6e4 55%,#9a8a70 78%,#4f4a42 100%)}
.hero-title{position:absolute;right:68px;top:96px;font-family:"Oswald",sans-serif;font-weight:500;font-size:40px;line-height:38px;color:var(--white);text-align:right}
.hero-arrow{position:absolute;top:124px;width:30px;height:30px;border-radius:50%;background:rgba(255,255,255,.75)}
.hero-arrow.prev{left:18px}.hero-arrow.next{right:18px}
.hero-arrow svg{position:absolute;left:9px;top:8px}
.box-dark{background:linear-gradient(#4a4a4c,#2d2d2f);border:1px solid #5a5a5c}
.box-title{font-family:"Oswald",sans-serif;font-size:16px;color:var(--white)}
.field-dark{background:#2a2220;border:1px solid #6a6a6a;height:18px}
.btn{display:inline-block;background:linear-gradient(#2c6bc0,var(--blue));color:var(--white);font-family:"Oswald",sans-serif;font-size:11px;text-align:center}
.keywords{left:171px;top:461px;width:229px;height:72px}
.newsletter{left:411px;top:461px;width:315px;height:72px}
.news-copy{position:absolute;left:16px;top:40px;width:220px;font-size:8.5px;line-height:11px;color:#e5e5e5}
.panel{background:var(--white);border:1px solid var(--line);border-radius:3px}
.panel-head{height:36px;background:linear-gradient(#2c63b0,var(--blue-deep));font-family:"Oswald",sans-serif;font-size:16px;color:var(--white);padding:6px 0 0 16px}
.quote{left:742px;top:462px;width:174px;height:178px}
.radio{position:absolute;top:46px;font-size:8px;font-weight:600;color:#444;display:flex;align-items:center;gap:5px}
.radio i{display:block;width:9px;height:9px;border:1px solid #777;border-radius:50%;position:relative}
.radio i.on::after{content:"";position:absolute;left:2px;top:2px;width:3px;height:3px;border-radius:50%;background:#555}
.q-field{position:absolute;left:18px;width:137px;height:17px;background:linear-gradient(#d4d4d4,#eaeaea);border:1px solid #c4c4c4;font-size:8px;color:#888;padding:3px 0 0 9px}
.featured{left:170px;top:543px;width:556px;height:35px;background:linear-gradient(#2c63b0,var(--blue-deep));border-radius:6px;font-family:"Oswald",sans-serif;color:var(--white)}
.featured-title{position:absolute;left:16px;top:7px;font-size:15px}
.pager{position:absolute;right:14px;top:6px;display:flex;align-items:center;gap:6px;font-size:14px}
.pager .cur{color:var(--gold)}
.card{position:absolute;width:174px;height:194px;background:var(--card);border:1px solid var(--line)}
.card-img{position:absolute;left:0;top:0;width:100%;height:132px;background:linear-gradient(#ffffff,#efefef);display:flex;align-items:center;justify-content:center}
.card-img span{display:block;width:140px;height:90px;border-radius:6px}
.card-name{position:absolute;top:137px;width:100%;text-align:center;font-size:11px;color:#333}
.card-btns{position:absolute;top:162px;left:12px;display:flex;gap:7px}
.card-btns .btn{height:22px;line-height:22px;font-size:10.5px}
.b-price{width:58px}.b-offer{width:84px}
.category{left:742px;top:652px;width:174px;height:184px}
.cat-item{position:absolute;left:0;width:100%;height:28px;border-bottom:1px solid #e4e4e4;font-size:8px;color:#333;padding:9px 0 0 32px}
.cat-item::before{content:"";position:absolute;left:14px;top:12px;width:4px;height:4px;border-radius:50%;background:#bbb}
.promo{left:742px;top:846px;width:174px;height:149px;background:linear-gradient(#f4f4f4 0%,#cfd3d8 55%,#2a2a2a 80%,#111 100%);border:1px solid var(--line)}
.footer{left:0;top:1040px;width:1087px;height:160px;background:linear-gradient(#2a5ea8,#1f4f96);font-family:"Lato",sans-serif;color:#dbe6f5}
.f-col{position:absolute;top:31px;font-size:10px;line-height:19px}
.f-col h4{font-size:11px;font-weight:700;color:var(--white);margin-bottom:10px}
.social{display:flex;gap:6px;margin-top:6px}
.social i{display:block;width:24px;height:24px;border-radius:50%;background:#e9eef6}
.f-legal{margin-top:14px;line-height:17px}
</style>
</head>
<body>
<div class="top-band"></div>

<div class="abs logo"><span class="logo-mark"></span><span class="logo-name">ByteGuard</span></div>
<div class="abs logo-tag">IT CONSULTING</div>
<div class="abs account"><a class="signin" href="#">Sign in</a><a class="register" href="#">Register</a></div>

<nav class="abs nav">
  <div class="nav-home"><svg width="16" height="15" viewBox="0 0 16 15"><path d="M8 1 L15 7 H13 V14 H10 V10 H6 V14 H3 V7 H1 Z" fill="#fff"/></svg></div>
  <a class="item" href="#">ABOUT</a>
  <a class="item" href="#">PRODUCTS</a>
  <a class="item" href="#">EXPLORE</a>
  <a class="item" href="#">PRICELISTS</a>
  <a class="item" href="#">CLIENTS</a>
  <a class="item" href="#">CONTACT US</a>
  <div class="nav-search">search<svg width="12" height="12" viewBox="0 0 12 12"><circle cx="5" cy="5" r="3.8" fill="none" stroke="#1d4a8c" stroke-width="1.8"/><path d="M8 8 L11 11" stroke="#1d4a8c" stroke-width="2"/></svg></div>
</nav>

<section class="abs hero" role="img" aria-label="Businessman with briefcase walking on an airfield beside a private plane, papers and a laptop flying in the air">
  <div class="hero-title">LORE<br>COMMOD</div>
  <div class="hero-arrow prev"><svg width="10" height="14" viewBox="0 0 10 14"><path d="M8 1 L2 7 L8 13" fill="none" stroke="#666" stroke-width="2.5"/></svg></div>
  <div class="hero-arrow next"><svg width="10" height="14" viewBox="0 0 10 14"><path d="M2 1 L8 7 L2 13" fill="none" stroke="#666" stroke-width="2.5"/></svg></div>
</section>

<section class="abs keywords box-dark">
  <div class="box-title abs" style="left:14px;top:9px">SEARCHED KEYWORKS</div>
  <div class="field-dark abs" style="left:17px;top:37px;width:137px"></div>
  <span class="btn abs" style="left:158px;top:37px;width:54px;height:18px;line-height:18px;font-family:'Open Sans',sans-serif;font-weight:600;font-size:9px">Search</span>
</section>

<section class="abs newsletter box-dark">
  <div class="box-title abs" style="left:16px;top:9px">EMAIL NEWSLETTER</div>
  <div class="field-dark abs" style="left:143px;top:13px;width:157px"></div>
  <p class="news-copy">Lorem ipsum dolor sit amet, consectetuer adipiscing elit. Aenean commodo ligula eget dolor.</p>
  <span class="btn abs" style="left:246px;top:41px;width:53px;height:18px;line-height:18px;font-family:'Open Sans',sans-serif;font-weight:600;font-size:9px">Subcribe</span>
</section>

<section class="abs quote panel">
  <div class="panel-head">GET THE PRODUCT QUOTE</div>
  <div class="radio" style="left:12px"><i class="on"></i>PUBLIC</div>
  <div class="radio" style="left:78px"><i></i>PRIVATE</div>
  <div class="q-field" style="top:63px">Product</div>
  <div class="q-field" style="top:85px">Name</div>
  <div class="q-field" style="top:107px">Mail Id</div>
  <div class="q-field" style="top:129px">Phone</div>
  <span class="btn abs" style="left:81px;top:151px;width:74px;height:18px;line-height:18px;font-family:'Open Sans',sans-serif;font-weight:600;font-size:9px">Get a Quote</span>
</section>

<section class="abs featured">
  <div class="featured-title">FEATURED PRODUCTS</div>
  <div class="pager">
    <svg width="7" height="10" viewBox="0 0 7 10"><path d="M6 0 L0 5 L6 10 Z" fill="#fff"/></svg>
    <span style="width:6px"></span><span class="cur">1</span><span>2</span><span>3</span><span style="width:6px"></span>
    <svg width="7" height="10" viewBox="0 0 7 10"><path d="M1 0 L7 5 L1 10 Z" fill="#fff"/></svg>
  </div>
</section>

<article class="card" style="left:171px;top:593px"><div class="card-img" role="img" aria-label="Silver laptop open, angled view"><span style="background:linear-gradient(#3a3a3a,#c9c9c9)"></span></div><div class="card-name">Corvo-Swift-256</div><div class="card-btns"><span class="btn b-price">PRICE LIST</span><span class="btn b-offer">LATEST OFFERINGS</span></div></article>
<article class="card" style="left:362px;top:593px"><div class="card-img" role="img" aria-label="Red and black laptops side by side"><span style="background:linear-gradient(90deg,#a01522,#2a2a2a)"></span></div><div class="card-name">Corvo-Swift-256</div><div class="card-btns"><span class="btn b-price">PRICE LIST</span><span class="btn b-offer">LATEST OFFERINGS</span></div></article>
<article class="card" style="left:552px;top:593px"><div class="card-img" role="img" aria-label="Black and red gaming laptop"><span style="background:linear-gradient(#8a1018,#1b1b1b)"></span></div><div class="card-name">Corvo-Swift-256</div><div class="card-btns"><span class="btn b-price">PRICE LIST</span><span class="btn b-offer">LATEST OFFERINGS</span></div></article>
<article class="card" style="left:171px;top:802px"><div class="card-img" role="img" aria-label="Silver laptop showing a tiled start screen"><span style="background:linear-gradient(#3c6fb5,#c8ccd2)"></span></div><div class="card-name">Corvo-Swift-256</div><div class="card-btns"><span class="btn b-price">PRICE LIST</span><span class="btn b-offer">LATEST OFFERINGS</span></div></article>
<article class="card" style="left:362px;top:802px"><div class="card-img" role="img" aria-label="Convertible laptop with a colourful tiled screen"><span style="background:linear-gradient(#6a3fa0,#2a2a30)"></span></div><div class="card-name">Corvo-Swift-256</div><div class="card-btns"><span class="btn b-price">PRICE LIST</span><span class="btn b-offer">LATEST OFFERINGS</span></div></article>
<article class="card" style="left:552px;top:802px"><div class="card-img" role="img" aria-label="3D laptop with a pair of 3D glasses"><span style="background:linear-gradient(#1d1d1d,#9aa2a6)"></span></div><div class="card-name">Corvo-Swift-256</div><div class="card-btns"><span class="btn b-price">PRICE LIST</span><span class="btn b-offer">LATEST OFFERINGS</span></div></article>

<section class="abs category panel">
  <div class="panel-head">PRODUCT CATEGORY</div>
  <div class="cat-item" style="top:37px">NOTEBOOKS</div>
  <div class="cat-item" style="top:65px">DESKTOPS</div>
  <div class="cat-item" style="top:93px">PRINTERS</div>
  <div class="cat-item" style="top:121px">POWER PRODUCTS</div>
  <div class="cat-item" style="top:149px;border-bottom:none">SOFTWARE</div>
</section>

<aside class="abs promo" role="img" aria-label="Promotional banner for a netbook at 60 percent off with a buy now button"></aside>

<footer class="abs footer">
  <div class="f-col" style="left:170px"><h4>Company</h4>Privacy<br>Terms Of Use<br>Terms Of Trade<br>PO T&amp;C's</div>
  <div class="f-col" style="left:294px"><h4>Marketing</h4>Customer Portals<br>Media Releases<br>News<br>Events</div>
  <div class="f-col" style="left:419px"><h4>Marketing</h4>Customer Portals<br>Media Releases<br>News<br>Events</div>
  <div class="f-col" style="left:534px;line-height:14.6px"><h4 style="margin-bottom:14px">Company Address</h4>
    Level 9 214 Harbour Lane<br>Eastbrook Vic 3999<br>
    T:&nbsp;&nbsp;&nbsp;&nbsp;&nbsp;+61 3 5550 1120<br>F:&nbsp;&nbsp;&nbsp;&nbsp;&nbsp;+61 3 5550 1145<br>E:&nbsp;&nbsp;&nbsp;&nbsp;&nbsp;hello@byteguard-it.example</div>
  <div class="f-col" style="left:720px"><h4>Follow Us Online</h4>
    <div class="social"><i></i><i></i><i></i><i></i></div>
    <div class="f-legal">Privacy Policy | Terms of Services | Sitemap<br>Copyright © 2012. All Rights Reserved.</div>
  </div>
</footer>
</body>
</html>
```